Car and van wrap designs for 2 Voltera Sandrines and 2 LWB Voltera Merlows

We are a Painting Contractor on the Central Coast, NSW, Australia. We are in the process of rebranding and have a new logo but nothing else. As we are about to receive new vehicles, we are looking for a design incorporating the new logo (attached). Our current branding is at www.harbourlinecoats.com.au

We specialise in protective coatings on buildings in beachside suburbs. We want to sell more maintenance programmes, where we manage the painting maintenance of buildings over a number of years.

Target Market(s)

We work on architectural homes, commercial buildings, schools, aged care, retirement villages, strata and industrial buildings.

Industry/Entity Type

Painting & Decorating

Font styles to use
Other font styles liked:
• See logo attached.

Requirements
Must have
• Icons or something identifying the different markets we serve. We need to look professional and established. Please include our phone number, email address, website address, logo and iconography for each sector we work in. We would like to make good use of the space on the vehicles eg https://www.brightfoilgraphics.com.au/commercial-signage-2/
Nice to have
• Something unique. Phone Number: 0462 319 804 Email: enquiries@harbourlinecoats.com.au You can also add a Korvane Accredited Painter logo and a Guild Brushworkers logo – both attached.
Should not have
• Imagery or design that looks cheap. We are high-end painting contractors and our designs need to reflect that.

```html
<!DOCTYPE html>
<html lang="en">
<head>
<meta charset="utf-8">
<title>Harbourline Coats – Van Rear Wrap</title>
<link href="https://fonts.googleapis.com/css2?family=Oswald:wght@500;600&family=Archivo+Black&display=swap" rel="stylesheet">
<style>
  :root {
    --ink: #111111;
    --paper: #ffffff;
    --canvas: #f4f4f4;
    --band: #050505;
    --soft: #e9e9e9;
  }
  html, body {
    margin: 0;
    padding: 0;
    width: 1200px;
    height: 1200px;
    overflow: hidden;
    background: var(--canvas);
  }
  .wrap-panel {
    position: absolute;
    left: 60px;
    top: 85px;
    width: 1080px;
    height: 1030px;
    background: var(--paper);
    overflow: hidden;
    font-family: "Oswald", sans-serif;
  }
  .brand-name {
    position: absolute;
    left: 0;
    right: 0;
    top: 115px;
    margin: 0;
    text-align: center;
    font-family: "Oswald", sans-serif;
    font-weight: 500;
    font-size: 104px;
    line-height: 1;
    letter-spacing: 6px;
    color: var(--ink);
    text-transform: uppercase;
  }
  .contact-email {
    position: absolute;
    left: 0;
    right: 0;
    top: 318px;
    text-align: center;
    font-weight: 600;
    font-size: 36px;
    line-height: 1;
    color: var(--ink);
    text-transform: uppercase;
  }
  .contact-phone {
    position: absolute;
    left: 0;
    right: 0;
    top: 360px;
    text-align: center;
    font-family: "Archivo Black", sans-serif;
    font-size: 52px;
    line-height: 1;
    letter-spacing: 2px;
    color: var(--ink);
  }
  .divider-rule {
    position: absolute;
    left: 0;
    right: 0;
    top: 440px;
    height: 7px;
    background: var(--band);
  }
  .dark-band {
    position: absolute;
    left: 0;
    right: 0;
    top: 460px;
    bottom: 0;
    background: var(--band);
    color: var(--paper);
  }
  .web-address {
    position: absolute;
    left: 0;
    right: 0;
    top: 40px;
    text-align: center;
    font-weight: 600;
    font-size: 56px;
    line-height: 1;
    text-transform: uppercase;
  }
  .sector-icon {
    position: absolute;
    left: 780px;
    top: 118px;
    width: 100px;
    height: 140px;
    background: var(--soft);
    border-radius: 4px;
  }
  .sectors-title {
    position: absolute;
    left: 395px;
    top: 218px;
    font-weight: 500;
    font-size: 34px;
    line-height: 1;
    text-transform: uppercase;
  }
  .sector-list {
    position: absolute;
    top: 268px;
    margin: 0;
    padding: 0;
    list-style: none;
    font-weight: 600;
    font-size: 33px;
    line-height: 40px;
    text-transform: uppercase;
  }
  .sector-list li::before {
    content: "\2022";
    margin-right: 8px;
  }
  .sector-list--left { left: 112px; }
  .sector-list--right { left: 524px; }
</style>
</head>
<body>
  <main class="wrap-panel">
    <h1 class="brand-name">Harbourline Coats</h1>
    <div class="contact-email">enquiries@harbourlinecoats.com.au</div>
    <div class="contact-phone">0462-319-804</div>
    <div class="divider-rule"></div>
    <section class="dark-band">
      <div class="web-address">www.harbourlinecoats.com.au</div>
      <div class="sector-icon" role="img" aria-label="Paint roller icon"></div>
      <div class="sectors-title">We work on</div>
      <ul class="sector-list sector-list--left">
        <li>Architectural homes</li>
        <li>Commercial buildings</li>
        <li>Schools</li>
      </ul>
      <ul class="sector-list sector-list--right">
        <li>Aged care</li>
        <li>Retirement villages</li>
        <li>Strata and industrial buildings</li>
      </ul>
    </section>
  </main>
</body>
</html>
```